K & R Ground Works. Business card design

We need a business card designed for a new business. We have a bulldozer and tractor service. We clear land and make wildlife food plots. We provide disking, bush hogging, and site prep services.
I have attached an image of a business card that I like and would like my business cards to look similar.

Target Market(s)

anyone needing bulldozer and/or tractor services

Industry/Entity Type

Business

Contact Information for Business Card

K & R Ground Works, Operated by 7-T-Ranch
Dale Whitcomb
601-555-0148
dwk4821@mailbarn.example

Font styles to use
Sans Serif

Colors

Designer to choose colors to be used in the design.

Requirements
Must have
• image of tractor and bulldozer
• Land Clearing
• Wildlife food plots
• Bush Hogging
• Disking
• Site prep
Nice to have
• i have included a image of a business card that i like. I would like mine to be similar.

```html
<!DOCTYPE html>
<html lang="en">
<head>
<meta charset="utf-8">
<title>K &amp; R Ground Works — Business Card</title>
<link rel="stylesheet" href="https://fonts.googleapis.com/css2?family=Oswald:wght@500;700&family=Exo+2:wght@500;600&display=swap">
<style>
  :root {
    --stage: #1b1b1d;
    --panel: #3a3a3c;
    --panel-dark: #1e1e20;
    --silver-light: #f4f4f4;
    --silver-mid: #b9b9bb;
    --silver-dark: #6d6d70;
    --sky: #7fb2e0;
    --foliage: #4f7a2e;
    --foliage-dark: #2f4c1c;
    --earth: #a88a5a;
    --title: #4a2c12;
    --text: #ffffff;
  }
  * { box-sizing: border-box; margin: 0; padding: 0; }
  html, body { width: 1200px; height: 900px; overflow: hidden; background: var(--stage); }
  .card {
    position: absolute; left: 100px; top: 164px;
    width: 1000px; height: 572px; overflow: hidden;
    border-radius: 6px; background: var(--panel-dark);
  }
  .card-photo {
    position: absolute; inset: 0 0 24px 0;
    background:
      linear-gradient(180deg, var(--sky) 0%, #a9cbe6 12%, var(--foliage) 34%, var(--foliage-dark) 62%, var(--earth) 100%);
  }
  .card-shapes { position: absolute; inset: 0; }
  .brand {
    position: absolute; left: 40px; top: 22px;
  }
  .brand-name {
    font-family: "Oswald", sans-serif; font-weight: 700;
    font-size: 44px; line-height: 1; letter-spacing: 1px;
    color: var(--title); text-transform: uppercase;
  }
  .brand-operator {
    margin-top: 8px;
    font-family: "Exo 2", sans-serif; font-weight: 600;
    font-size: 24px; letter-spacing: 2px; color: var(--text);
    text-transform: uppercase;
  }
  .contact { position: absolute; left: 40px; top: 306px; color: var(--text); }
  .contact-name {
    font-family: "Exo 2", sans-serif; font-weight: 600;
    font-size: 30px; letter-spacing: 2px; text-transform: uppercase;
    margin-bottom: 14px;
  }
  .contact-line {
    display: flex; align-items: center; gap: 10px;
    font-family: "Exo 2", sans-serif; font-weight: 500;
    font-size: 21px; margin-bottom: 8px;
  }
  .contact-icon { width: 22px; height: 22px; flex: none; }
  .mark {
    position: absolute; left: 373px; top: 283px;
    width: 124px; height: 124px; border-radius: 50%;
    background: var(--silver-mid);
    display: flex; align-items: center; justify-content: center;
    font-family: "Oswald", sans-serif; font-weight: 700;
    font-size: 34px; color: var(--panel-dark);
  }
  .services {
    position: absolute; right: 40px; top: 384px;
    list-style: none; text-align: right;
  }
  .services li {
    display: flex; justify-content: flex-end; align-items: center; gap: 12px;
    font-family: "Oswald", sans-serif; font-weight: 700;
    font-size: 24px; line-height: 31px; color: var(--text);
    text-transform: uppercase; letter-spacing: 0.5px;
  }
  .services li::after {
    content: ""; width: 12px; height: 12px; border-radius: 50%;
    background: var(--text);
  }
</style>
</head>
<body>
  <main class="card">
    <div class="card-photo" role="img" aria-label="Photo of a red tractor on the left and a yellow bulldozer with raised blade on the right, in a cleared field with trees and blue sky"></div>

    <svg class="card-shapes" width="1000" height="572" viewBox="0 0 1000 572" aria-hidden="true">
      <defs>
        <linearGradient id="silver" x1="0" y1="0" x2="0" y2="1">
          <stop offset="0" stop-color="var(--silver-dark)"/>
          <stop offset="0.5" stop-color="var(--silver-light)"/>
          <stop offset="1" stop-color="var(--silver-dark)"/>
        </linearGradient>
      </defs>
      <polygon points="0,290 395,290 470,370 1000,370 1000,572 0,572" fill="var(--panel)"/>
      <polyline points="0,290 395,290 470,370 1000,370" fill="none" stroke="url(#silver)" stroke-width="9"/>
      <rect x="0" y="546" width="1000" height="12" fill="url(#silver)"/>
      <rect x="0" y="558" width="1000" height="14" fill="var(--panel-dark)"/>
    </svg>

    <header class="brand">
      <h1 class="brand-name">K &amp; R Ground Works</h1>
      <p class="brand-operator">Operated by 7-T-Ranch</p>
    </header>

    <div class="mark">K&amp;R</div>

    <section class="contact">
      <p class="contact-name">Dale Whitcomb</p>
      <p class="contact-line">
        <svg class="contact-icon" viewBox="0 0 24 24" aria-hidden="true">
          <circle cx="12" cy="12" r="11" fill="#fff"/>
          <path d="M8.5 6.5l2 2.2-1.2 1.6c.8 1.6 2 2.8 3.6 3.6l1.6-1.2 2.2 2-1.3 1.8c-4.3-.4-8.2-4.3-8.6-8.6z" fill="var(--panel)"/>
        </svg>
        601-555-0148
      </p>
      <p class="contact-line">
        <svg class="contact-icon" viewBox="0 0 24 24" aria-hidden="true">
          <circle cx="12" cy="12" r="11" fill="#fff"/>
          <rect x="6" y="8" width="12" height="8" fill="var(--panel)"/>
          <path d="M6 8l6 5 6-5" fill="none" stroke="#fff" stroke-width="1.3"/>
        </svg>
        dwk4821@mailbarn.example
      </p>
    </section>

    <ul class="services">
      <li>Land Clearing</li>
      <li>Wildlife Food Plots</li>
      <li>Bush Hogging</li>
      <li>Disking</li>
      <li>Site Prep</li>
    </ul>
  </main>
</body>
</html>
```